New Flyer Design Project

We need a flyer for our upcoming Rising Builders Forum.

5th Annual Rising Builders Forum
by the Council for Stewardship of Built Ventures (C-SBuV)
Theme: Step Forward
Date: January 24, 2020
Location: Bluestone Lodge Hotel and Conference Center, San Marcos, TX
#StepForward

This is event is put together by C-SBuV's Rising Builders Ring of Merit. I have a logo for the Ring of Merit, but not something that indicates it's the Rising Builders Ring.

More about the Forum (please don't include on the flyer): This Forum provides a venue to openly discuss issues affecting women in our industry and ideas and strategies to address those issues.

Architecture, Construction and Engineering are all struggling with a tremendous shortage of skilled talent. It is more important than ever for organizations to be able to attract, support and retain a talented workforce and to encourage more women to pursue and build vibrant careers in architecture, engineering and construction. Unfortunately, their attrition rate also remains high in these industries. Developing and retaining a skilled workforce includes identifying and addressing the specific needs of women in our industry. Man or Woman; Male or Female Brain, C-SBuV’s Rising Builders Forum will give you and your team the tools you need to excel as an Employer of Choice and a roadmap for individual continued career planning and success .

This unique Forum provides a venue to engage everyone from executives to those just beginning their careers with active, hands-on sessions and vibrant networking with the best and brightest in the A/E/C industry. In our usual C-SBuV Forum style, Keynotes become table participants and table participants become presenters, encouraging participants to assimilate what they are learning. Join local, state and national leaders and subject matter experts as we candidly explore and address the issues affecting women in our industry .

```html
<!DOCTYPE html>
<html lang="en">
<head>
<meta charset="utf-8">
<title>5th Annual Rising Builders Forum</title>
<link rel="stylesheet" href="https://fonts.googleapis.com/css2?family=Montserrat:ital,wght@0,400;0,700;0,800;1,400;1,900&display=swap">
<style>
  :root {
    --navy: #1f3f8f;
    --blue: #2a63e6;
    --deep-blue: #0b2aa8;
    --yellow: #ffe500;
    --cyan: #2fd0e8;
    --green: #3ee83a;
    --olive: #c8c800;
    --grey: #5a5a5a;
    --white: #ffffff;
  }
  * { margin: 0; padding: 0; box-sizing: border-box; }
  html, body { width: 848px; height: 1200px; overflow: hidden; background: var(--white); }
  body { font-family: "Montserrat", sans-serif; }
  .flyer { position: relative; width: 848px; height: 1200px; overflow: hidden; background: var(--white); }

  .hero-photo {
    position: absolute; inset: 0 0 auto 0; height: 842px;
    clip-path: polygon(0 0, 100% 0, 100% 710px, 0 842px);
    background: linear-gradient(90deg, var(--cyan) 0%, #3ecfe0 22%, #d6c85a 35%, #f0e13c 55%, var(--green) 68%, var(--green) 100%);
  }

  .headline {
    position: absolute; left: 48px; top: 392px;
    transform: rotate(-10deg); transform-origin: left top;
    font-weight: 900; font-style: italic; color: var(--white);
    line-height: .88; letter-spacing: -3px; white-space: nowrap;
    text-shadow:
      2px 0 0 var(--deep-blue), -2px 0 0 var(--deep-blue),
      0 2px 0 var(--deep-blue), 0 -2px 0 var(--deep-blue),
      2px 2px 0 var(--deep-blue), -2px -2px 0 var(--deep-blue),
      2px -2px 0 var(--deep-blue), -2px 2px 0 var(--deep-blue),
      -7px 5px 0 var(--blue);
  }
  .headline-small { display: block; font-size: 74px; margin-left: 40px; }
  .headline-large { display: block; font-size: 122px; }

  .edition {
    position: absolute; left: 196px; top: 664px; width: 420px; height: 250px;
    font-weight: 900; font-style: italic; color: var(--yellow); line-height: 1;
  }
  .edition-number { position: absolute; left: 0; top: 0; font-size: 280px; letter-spacing: -6px; }
  .edition-suffix {
    position: absolute; left: 168px; top: 10px; font-size: 168px; letter-spacing: -6px;
    text-shadow: 3px 0 0 var(--white), -3px 0 0 var(--white), 0 3px 0 var(--white), 0 -3px 0 var(--white);
  }

  .event-title {
    position: absolute; right: 81px; top: 822px; text-align: right;
    color: var(--navy); font-weight: 800; font-size: 43px; line-height: 1.13; letter-spacing: 1px;
  }
  .host-line {
    position: absolute; right: 81px; top: 919px; text-align: right;
    color: var(--navy); font-weight: 700; font-size: 15.5px; letter-spacing: .4px;
  }
  .venue {
    position: absolute; right: 78px; top: 956px; text-align: right;
    color: var(--navy); font-weight: 800; font-size: 22.5px; line-height: 1.25; letter-spacing: .8px;
  }
  .venue-date { color: var(--yellow); font-size: 38px; font-weight: 700; letter-spacing: 0; vertical-align: -8px; }

  .org-mark { position: absolute; display: flex; flex-direction: column; align-items: center; }
  .org-mark-council { left: 32px; top: 968px; width: 236px; }
  .org-mark-ring { left: 306px; top: 1058px; width: 222px; }
  .org-mark-circle { border-radius: 50%; background: var(--navy); }
  .org-mark-council .org-mark-circle { width: 106px; height: 106px; }
  .org-mark-ring .org-mark-circle { width: 64px; height: 64px; }
  .org-mark-name { color: var(--grey); font-weight: 400; margin-top: 12px; white-space: nowrap; }
  .org-mark-council .org-mark-name { font-size: 46px; letter-spacing: -1px; }
  .org-mark-ring .org-mark-name { font-size: 24px; }

  .theme { position: absolute; left: 628px; top: 1122px; color: var(--navy); }
  .theme-label { display: block; font-style: italic; font-size: 15px; }
  .theme-tag { display: block; font-style: italic; font-weight: 900; font-size: 19px; }
</style>
</head>
<body>
<main class="flyer">
  <div class="hero-photo" role="img" aria-label="Photo of a woman in a yellow hard hat and safety vest holding blueprints, flanked by cyan and green tinted repeats of the same figure on a construction site"></div>

  <h1 class="headline">
    <span class="headline-small">STEP</span>
    <span class="headline-large">FORWARD</span>
  </h1>

  <div class="edition">
    <span class="edition-number">5</span><span class="edition-suffix">TH</span>
  </div>

  <h2 class="event-title">ANNUAL RISING<br>BUILDERS FORUM</h2>
  <p class="host-line">by the Council for Stewardship of Built Ventures (C-SBuV)</p>

  <p class="venue">@ BLUESTONE LODGE HOTEL<br>AND CONFERENCE CENTER,<br>SAN MARCOS, TX <span class="venue-date">Jan 24</span></p>

  <div class="org-mark org-mark-council">
    <span class="org-mark-circle"></span>
    <span class="org-mark-name">C-SBuV</span>
  </div>

  <div class="org-mark org-mark-ring">
    <span class="org-mark-circle"></span>
    <span class="org-mark-name">Ring of Merit</span>
  </div>

  <p class="theme">
    <span class="theme-label">Theme:</span>
    <span class="theme-tag">#Step Forward</span>
  </p>
</main>
</body>
</html>
```